Skin Care Branding / Package design

We are a manufacturer of consumable hemp products and have some skin care products we want to group into a brand of its own, under our primary brand which is TulaMoss.  our website is www.tulamossgoods.example
Our current packaging was developed on the fly with little or no thought given to a sub brand concept.  We have sub branded other products such as Quiet Fern, Willow Crest, and Harbin.  While TulaMoss appears on the packaging it is not the predominate brand.
The products will be sold in cosmetic stores, health stores, medspas, pharmacies and other upscale stores.  We want the appeal to be elegant & upscale and stand out on the shelf.
We are open to changing the jar, bottle or container and look forward to any recommendations on this.
Later we will need flyers, social media ads, and other graphics.
Our primary goal is to create designs for each of our products that are consistent and create another sub brand.
We are also open to changing the names of these products.
images of the existing products are attached, we plan to add more skin care products.

```html
<!DOCTYPE html>
<html lang="en">
<head>
<meta charset="utf-8">
<title>TulaMoss Calming Lotion Label</title>
<link rel="stylesheet" href="https://fonts.googleapis.com/css2?family=Barlow+Semi+Condensed:wght@400;500;600;700&family=Barlow+Condensed:wght@500&display=swap">
<style>
  :root {
    --page: #ffffff;
    --label: #dbd8d3;
    --label-edge: #cfcbc5;
    --ink: #2c2c2c;
    --ink-soft: #5a5a5a;
    --brand-grey: #6a6a6a;
    --lavender-light: #a897b6;
    --lavender-deep: #76598a;
    --script-tone: #c9c5bf;
  }
  * { margin: 0; padding: 0; box-sizing: border-box; }
  html, body {
    width: 1200px;
    height: 1200px;
    overflow: hidden;
    background: var(--page);
  }
  .label {
    position: absolute;
    left: 180px;
    top: 75px;
    width: 840px;
    height: 1050px;
    background: linear-gradient(90deg, var(--label-edge) 0%, var(--label) 18%, var(--label) 82%, var(--label-edge) 100%);
    font-family: "Barlow Semi Condensed", sans-serif;
    color: var(--ink);
  }
  .sub-brand-script {
    position: absolute;
    left: 150px;
    top: 116px;
    width: 322px;
    height: 97px;
    background: linear-gradient(90deg, var(--script-tone), var(--label));
    border-radius: 6px;
  }
  .product-name {
    position: absolute;
    left: 148px;
    top: 356px;
    font-size: 94px;
    font-weight: 600;
    letter-spacing: -1px;
    line-height: 1;
  }
  .scent-tag {
    position: absolute;
    left: 147px;
    top: 486px;
    width: 363px;
    height: 92px;
    background: linear-gradient(90deg, var(--lavender-light), var(--lavender-deep));
    color: #f4f0f6;
    font-size: 66px;
    font-weight: 400;
    line-height: 92px;
    padding-left: 28px;
  }
  .potency {
    position: absolute;
    left: 148px;
    top: 668px;
    font-size: 74px;
    font-weight: 700;
    line-height: 1;
  }
  .blend {
    position: absolute;
    left: 150px;
    top: 758px;
    font-size: 50px;
    font-weight: 400;
    color: var(--ink-soft);
    line-height: 1;
  }
  .divider {
    position: absolute;
    left: 150px;
    top: 838px;
    width: 520px;
    height: 3px;
    background: var(--ink);
  }
  .descriptor {
    position: absolute;
    left: 150px;
    top: 860px;
    font-size: 50px;
    font-weight: 500;
    line-height: 1;
  }
  .brand-mark {
    position: absolute;
    left: 150px;
    top: 1000px;
    display: flex;
    align-items: center;
    gap: 12px;
    transform: translateY(-50%);
  }
  .brand-mark .brand-name {
    font-size: 44px;
    font-weight: 700;
    color: var(--brand-grey);
    line-height: 1;
  }
  .brand-mark .brand-dot {
    width: 26px;
    height: 26px;
    border-radius: 50%;
    background: var(--brand-grey);
  }
  .net-weight {
    position: absolute;
    right: 175px;
    top: 1002px;
    font-family: "Barlow Condensed", sans-serif;
    font-weight: 500;
    font-size: 32px;
    color: var(--ink);
    line-height: 1;
  }
</style>
</head>
<body>
  <section class="label">
    <div class="sub-brand-script" role="img" aria-label="Hand-lettered sub-brand script wordmark"></div>
    <h1 class="product-name">CALMING LOTION</h1>
    <div class="scent-tag">Lavender</div>
    <p class="potency">CBD+CBG | 800mg</p>
    <p class="blend">50 / 50 bland</p>
    <div class="divider"></div>
    <p class="descriptor">Infused Daily Moisturizer</p>
    <div class="brand-mark">
      <span class="brand-name">TulaMoss</span>
      <span class="brand-dot"></span>
    </div>
    <p class="net-weight">Net.Wt 4 fl.oz / 120 ml</p>
  </section>
</body>
</html>
```